Delia Vornholt Resume 2025

🎨 Design Aesthetic
Overall Look: Sophisticated, clean, minimalist — less “corporate template,” more “editorial/luxury brand.” Think Interior Ledger meets Calloway’s Worldwide Estates.
Colors:
Base: Warm white or ivory background (instead of stark white, which can feel clinical).
Accents: Soft taupe, blush beige, muted rose-gold, warm gray. These lean feminine, elegant, and upscale without being distracting.
Avoid heavy blacks — use charcoal gray for text.
🔤 Typography
You’ll want fonts that are timeless, system-available (no downloading), and upscale. Pairing one serif with one sans-serif is a proven high-end combo.
Primary Serif (for Name + Section Headers):
Georgia (classic, built-in)
Times New Roman (if you want ultra-traditional, though a bit expected)
Palatino Linotype (a softer, elegant serif)
Secondary Sans-serif (for body text):
Helvetica Neue (clean, luxury feel)
Calibri (simple, highly readable, professional)
Arial Narrow (refined but modern)
✨ Recommended pairing: Name/Headings in Georgia Bold + Body in Helvetica Neue Light → refined, professional, easy to use in all your collateral.
📐 Layout & Structure
Header (Top Third):
Your name large, centered or left-aligned.
Subline with phone, email, location in smaller font, spaced out with dividers (e.g., |).
Neutral line or subtle accent bar under the header (warm gray or muted blush).
Section Layout:
Plenty of white space (breathe between sections, upscale feel).
Clear section headers (all caps serif font, spaced letters for luxury look).
Use subtle horizontal rules in a soft accent color instead of thick lines.
Accents:
Very subtle shading in soft beige or blush for section backgrounds (not blocks, just highlights).
Icons kept minimal — avoid anything too “clip-arty.”
🖼 Visual Mood Reference
Imagine:
A high-end boutique hotel brand sheet
Varnel packaging tones (ivory, taupe, gold accent) but dialed down to be subtle
Editorial spacing like in Lustre or Nova Interiors
🗂 Sections to Highlight (for your pivot)
Profile / Objective – Short 2–3 lines at the top making clear you are pivoting into luxury real estate, with transferable leadership skills.
Experience – TKW Media (as Owner, not Managing Partner) with emphasis on entrepreneurship, strategy, client growth.
Board Membership – Vornholt Foundation role (philanthropy adds prestige).
Certifications – Shows discipline and learning.
Education – Clean, simple.
“I want a resume design that feels refined and luxury-oriented, clean and sophisticated, with soft neutral feminine tones (ivory, blush beige, taupe, warm gray). Font pairing should be elegant but standard (e.g., Georgia for headings + Helvetica Neue for body) so I can reuse across collateral without downloading special fonts. Layout should have lots of white space, understated lines/dividers, and feel like something you’d expect from a luxury real estate or fashion brand.”
Real Estate Brokerage Houses
Real Estate - Luxury

```html
<!DOCTYPE html>
<html lang="en">
<head>
<meta charset="UTF-8">
<title>Delia Vornholt – Resume</title>
<link href="https://fonts.googleapis.com/css2?family=Open+Sans:wght@300;400;600;700&display=swap" rel="stylesheet">
<style>
  :root {
    --paper: #ffffff;
    --panel: #fdf3ec;
    --band: #9a9a9a;
    --ink: #3a3a3a;
    --heading: #6b6b6b;
    --body: #7b7b7b;
    --dark: #1e1e1e;
    --photo-a: #cfcfcf;
    --photo-b: #4a4a4a;
  }
  * { margin: 0; padding: 0; box-sizing: border-box; }
  html, body { width: 850px; height: 1200px; overflow: hidden; background: var(--paper); }
  body { position: relative; font-family: "Open Sans", Arial, sans-serif; color: var(--body); }
  .abs { position: absolute; }

  .corner-block { left: 0; top: 0; width: 68px; height: 67px; background: var(--band); }
  .side-panel { left: 0; top: 67px; width: 299px; height: 1111px; background: var(--panel); }
  .footer-band { left: 68px; top: 1178px; width: 755px; height: 12px; background: var(--band); }

  .portrait { left: 68px; top: 68px; width: 192px; height: 229px;
    background: radial-gradient(ellipse at 50% 40%, var(--photo-a) 0%, #9d9d9d 45%, var(--photo-b) 100%); }

  .name { left: 68px; top: 312px; font-size: 20.5px; font-weight: 700; color: var(--heading); letter-spacing: .2px; }
  .title { left: 68px; top: 340px; font-size: 11.5px; color: var(--body); letter-spacing: .5px; }

  .side-heading { font-size: 15.5px; font-weight: 400; color: var(--dark); letter-spacing: .3px; }
  .side-heading.light { color: var(--heading); }
  .contacts-heading { left: 65px; top: 394px; }
  .address { left: 65px; top: 424px; font-size: 12.5px; line-height: 16.5px; color: var(--ink); }

  .contact-row { left: 66px; display: flex; align-items: center; font-size: 12.5px; color: var(--heading); height: 16px; }
  .contact-row svg { width: 14px; height: 14px; margin-right: 29px; fill: var(--dark); }
  .contact-row .square { width: 11px; height: 11px; background: var(--dark); margin: 0 32px 0 1px; }

  .section-icon { fill: var(--dark); }
  .edu-icon { left: 65px; top: 602px; }
  .edu-heading { left: 104px; top: 599px; }
  .school { left: 65px; top: 639px; font-size: 13px; font-weight: 700; color: var(--heading); letter-spacing: .3px; }
  .degree { left: 66px; top: 663px; font-size: 12.5px; line-height: 18px; color: var(--ink); }

  .cert-icon { left: 68px; top: 735px; }
  .cert-heading { left: 107px; top: 737px; color: var(--dark); }
  .cert-list { left: 78px; top: 777px; width: 215px; list-style: none; font-size: 11.8px; line-height: 17.6px; color: var(--heading); }
  .cert-list li { position: relative; padding-left: 26px; margin-bottom: 17px; }
  .cert-list li::before { content: ""; position: absolute; left: 0; top: 7px; width: 3px; height: 3px; background: var(--body); }

  .main-heading { font-size: 16.5px; color: var(--dark); font-weight: 400; letter-spacing: .2px; }
  .profile-icon { left: 349px; top: 177px; }
  .profile-heading { left: 389px; top: 176px; }
  .profile-text { left: 349px; top: 215px; width: 414px; font-size: 11.8px; line-height: 16.3px; text-align: justify; color: var(--body); }
  .profile-text p + p { margin-top: 16px; }

  .timeline { width: 1.5px; background: var(--dark); }
  .timeline-dot { width: 7px; height: 7px; border-radius: 50%; background: var(--dark); }

  .work-icon { left: 349px; top: 424px; }
  .work-heading { left: 392px; top: 422px; font-size: 15.5px; }
  .company { font-size: 18px; font-weight: 700; color: var(--heading); letter-spacing: .2px; }
  .dates { font-size: 12.5px; color: var(--ink); text-align: right; }
  .role { left: 394px; top: 481px; font-size: 14px; font-weight: 300; color: var(--body); letter-spacing: .4px; }
  .work-text { left: 392px; top: 504px; width: 395px; font-size: 12px; line-height: 16.3px; color: var(--ink); text-align: justify; }
  .accomplish-heading { left: 392px; top: 619px; font-size: 13.5px; font-weight: 700; color: var(--heading); }
  .bullets { list-style: none; font-size: 11.8px; line-height: 16.3px; color: var(--body); text-align: justify; }
  .bullets li { position: relative; margin-bottom: 1.8px; }
  .bullets li::before { content: ""; position: absolute; left: -24px; top: 5px; width: 4px; height: 4px; background: var(--body); }
  .work-bullets { left: 446px; top: 639px; width: 341px; }

  .board-icon { left: 347px; top: 863px; }
  .board-heading { left: 389px; top: 867px; font-size: 15.5px; }
  .board-role { left: 389px; top: 919px; width: 402px; font-size: 15px; font-weight: 300; line-height: 24px; color: var(--heading); text-transform: uppercase; text-align: justify; text-align-last: left; letter-spacing: .2px; }
  .board-bullets { left: 455px; top: 981px; width: 328px; line-height: 17.6px; text-align: left; }
  .board-bullets li { margin-bottom: 1.5px; }
  .board-bullets li::before { left: -25px; top: 6px; }
  .board-bullets li:first-child { color: var(--ink); }
</style>
</head>
<body>
  <div class="abs corner-block"></div>
  <div class="abs side-panel"></div>
  <div class="abs footer-band"></div>

  <!-- Sidebar -->
  <div class="abs portrait" role="img" aria-label="Portrait photograph of Delia Vornholt"></div>
  <div class="abs name">DELIA VORNHOLT</div>
  <div class="abs title">TITLE</div>

  <div class="abs side-heading contacts-heading">CONTACTS</div>
  <div class="abs address">318 Larkmoor Lane<br>Ashford, TN&nbsp; 37900</div>

  <div class="abs contact-row" style="top:471px">
    <svg viewBox="0 0 16 16"><path d="M1 3h14v10H1z M1 3l7 5 7-5" fill="none" stroke="#1e1e1e" stroke-width="1.6"/></svg>
    delia@tkwmedia.example
  </div>
  <div class="abs contact-row" style="top:493px">
    <svg viewBox="0 0 16 16"><path d="M3 1l3 3-1.5 2.2c1 2 2.5 3.5 4.3 4.3L11 9l3 3-2 2.5C6.5 14 2 9.5 1.5 3.5z"/></svg>
    (555) 014-2876
  </div>
  <div class="abs contact-row" style="top:514px">
    <svg viewBox="0 0 16 16"><g fill="none" stroke="#1e1e1e" stroke-width="1.3"><circle cx="8" cy="8" r="6.5"/><ellipse cx="8" cy="8" rx="3" ry="6.5"/><path d="M1.5 8h13M2.5 4.5h11M2.5 11.5h11"/></g></svg>
    www.deliavornholt.example
  </div>
  <div class="abs contact-row" style="top:534px">
    <span class="square"></span>
    profile: deliavornholt
  </div>

  <svg class="abs section-icon edu-icon" width="18" height="14" viewBox="0 0 18 14"><path d="M1 2c3-1 6-1 8 1 2-2 5-2 8-1v11c-3-1-6-1-8 1-2-2-5-2-8-1z M9 3v11" fill="none" stroke="#1e1e1e" stroke-width="1.5"/></svg>
  <div class="abs side-heading light edu-heading">EDUCATION</div>
  <div class="abs school">HALDEN UNIVERSITY</div>
  <div class="abs degree">Bachelor of Arts, Sociology<br>1993 – 1998</div>

  <svg class="abs section-icon cert-icon" width="18" height="17" viewBox="0 0 18 17"><path d="M1 0v16h17 M3 12l3-5 3 3 3-6 3 2 2-3" fill="none" stroke="#1e1e1e" stroke-width="1.4"/></svg>
  <div class="abs side-heading cert-heading">CERTIFICATIONS</div>
  <ul class="abs cert-list">
    <li>Leadership for Sales &amp; Marketing Professionals – Corvane Learning Group, 2018</li>
    <li>Scaling Excellence Across the Organization – Corvane Learning Group, 2019</li>
    <li>Mailrise Email &amp; Inbound Marketing Certifications – 2019</li>
    <li>Executive Playbook: Managing Change, Conflict &amp; Communications – Corvane, 2019</li>
    <li>21st Century Leadership – Corvane Learning Group, 2020</li>
  </ul>

  <!-- Profile -->
  <svg class="abs section-icon profile-icon" width="20" height="18" viewBox="0 0 20 18"><circle cx="10" cy="5" r="4.5"/><path d="M1 18c0-5 3-7 6-7.5l3 2 3-2c3 .5 6 2.5 6 7.5z"/></svg>
  <div class="abs main-heading profile-heading">PERSONAL PROFIL</div>
  <div class="abs profile-text">
    <p>Delia Vornholt is an industry-leading media strategist and entrepreneur with 15+ years of experience across multiple industries. As Owner of the award-winning EDWOSB-certified agency TKW Media Inc., she drives performance across multiple departments and acts as an internal strategic advisor. Her expertise spans government project management and corporate workflows, providing a rare combination of entrepreneurship, leadership, and marketing strategy.</p>
    <p>Delia is now pursuing a full-time career in real estate, bringing her skills in negotiation, business development, and client relations to the Miami luxury market.</p>
  </div>

  <!-- Work -->
  <svg class="abs section-icon work-icon" width="18" height="17" viewBox="0 0 18 17"><path d="M6 3V1h6v2h5v13H1V3z M7 3h4V2H7z"/><rect x="1" y="8" width="16" height="1.5" fill="#fff"/></svg>
  <div class="abs main-heading work-heading">WORK EXPERIENCE</div>
  <div class="abs timeline" style="left:357px; top:440px; height:373px"></div>
  <div class="abs timeline-dot" style="left:354.5px; top:464.5px"></div>
  <div class="abs company" style="left:394px; top:454px">TKW MEDIA, INC.</div>
  <div class="abs dates" style="left:662px; top:461px; width:120px">2007 – Present</div>
  <div class="abs role">OWNER</div>
  <div class="abs work-text">As a business owner in the media and marketing space, Delia brings innovative insight and marketing ideas, becoming an industry expert for every client. Her creativity, flexibility, transparency, and results-driven approach lend to long-term partnerships across all business verticals. By working closely with clients, her teams create powerful media and marketing campaigns that engage and inspire.</div>
  <div class="abs accomplish-heading">Key Accomplishments</div>
  <ul class="abs bullets work-bullets">
    <li>Scaled TKW Media Inc.’s client base both commercially and federally during the COVID-19 pandemic.</li>
    <li>Conceptualized and organized large-scale campaigns while leading TKW to immense success despite market disruptions.</li>
    <li>Directed regional defense service campaigns across 13+ states in the past 12 months.</li>
    <li>For the Northland Regional Guard, overhauled marketing efforts to be data-driven and high-performing, delivering 3M+ impressions, 700+ conversions (2.58% conversion rate), and a 533% decreased CPA (from $901 to $48 at launch).</li>
  </ul>

  <!-- Board -->
  <svg class="abs section-icon board-icon" width="20" height="14" viewBox="0 0 20 14"><circle cx="4" cy="3.5" r="2.3"/><circle cx="16" cy="3.5" r="2.3"/><circle cx="10" cy="3" r="2.8"/><path d="M0 11c0-3 1.5-4.5 4-4.5s4 1.5 4 4.5z M12 11c0-3 1.5-4.5 4-4.5s4 1.5 4 4.5z M5 14c0-4 2-6 5-6s5 2 5 6z"/></svg>
  <div class="abs main-heading board-heading">BOARD MEMBERSHIP</div>
  <div class="abs timeline" style="left:356.5px; top:882px; height:11px"></div>
  <div class="abs timeline-dot" style="left:354px; top:895.5px"></div>
  <div class="abs timeline" style="left:356.5px; top:904px; height:199px"></div>
  <div class="abs company" style="left:388px; top:885px">THE VORNHOLT FOUNDATION</div>
  <div class="abs dates" style="left:672px; top:889px; width:120px">2018 – Present</div>
  <div class="abs board-role">Active board member, The Marguerite Vornholt &amp; Edmund R. Vornholt Memorial Foundation</div>
  <ul class="abs bullets board-bullets">
    <li>Support governance, fundraising, and philanthropic initiatives dedicated to advancing music education and instrument preservation.</li>
    <li>Collaborate with fellow board members to ensure compliance, organizational growth, and mission alignment.</li>
    <li>Represent family legacy and oversee strategic initiatives benefiting communities nationwide.</li>
  </ul>
</body>
</html>
```